Civil engineering company | Billboard

We need a billboard design for Velmora- civil engineering company. We want big logo in the center of billboard and web site (www.velmora.hr) below the logo. Also, we want an subtle abstract pattern in the background. Dimensions of the billboard are: width :10 m, height: 2m. Design must be celan and modern.
Industry/Entity Type
Civil engineering
Font styles to use
Sans Serif
Colors
F0912C
F2A743
F7CA91
FBE8D2
FDF5EE
Requirements
Must have
- Logo and new unique pattern design for Velmroa company
Should not have
- pictures of construction machinery and tools

```html
<!DOCTYPE html>
<html lang="en">
<head>
<meta charset="utf-8">
<title>Velmora Billboard</title>
<link href="https://fonts.googleapis.com/css2?family=Montserrat:wght@400;500&display=swap" rel="stylesheet">
<style>
  :root {
    --orange: #e8923a;
    --orange-light: #f2a743;
    --orange-deep: #f0912c;
    --ink: #3a3a3c;
    --grey-mark: #6b6b6d;
    --paper: #ffffff;
    --night: #231f20;
    --stage: #eef0f3;
  }
  * { margin: 0; padding: 0; box-sizing: border-box; }
  html, body {
    width: 720px;
    height: 1200px;
    overflow: hidden;
    background: var(--stage);
  }
  .canvas {
    width: 720px;
    height: 1200px;
    display: flex;
    flex-direction: column;
    justify-content: center;
    align-items: center;
    gap: 160px;
  }
  .billboard {
    position: relative;
    width: 680px;
    height: 136px;
    overflow: hidden;
  }
  .billboard--light { background: var(--paper); }
  .billboard--dark { background: var(--night); }
  .brand-square {
    position: absolute;
    left: 44px;
    top: 32px;
    width: 72px;
    height: 72px;
    border: 2px solid var(--grey-mark);
  }
  .brand-name {
    position: absolute;
    left: 124px;
    top: 30px;
    font-family: "Montserrat", sans-serif;
    font-weight: 500;
    font-size: 50px;
    line-height: 1;
    letter-spacing: 3px;
    text-transform: uppercase;
    color: var(--orange);
  }
  .web-address {
    position: absolute;
    left: 156px;
    top: 80px;
    font-family: "Montserrat", sans-serif;
    font-weight: 400;
    font-size: 22px;
    line-height: 1;
    letter-spacing: 4px;
  }
  .billboard--light .web-address { color: var(--ink); }
  .billboard--dark .web-address { color: var(--paper); }
  .pattern-field {
    position: absolute;
    right: 0;
    top: 0;
    width: 680px;
    height: 136px;
  }
</style>
</head>
<body>
  <main class="canvas">
    <section class="billboard billboard--light">
      <div class="brand-square"></div>
      <div class="brand-name">Velmora</div>
      <div class="web-address">www.velmora.hr</div>
      <svg class="pattern-field" viewBox="0 0 680 136" role="img" aria-label="Orange geometric chevron pattern in the right corner">
        <defs>
          <linearGradient id="patternLight" x1="0" y1="1" x2="1" y2="0">
            <stop offset="0" stop-color="var(--orange-deep)"/>
            <stop offset="1" stop-color="var(--orange-light)"/>
          </linearGradient>
        </defs>
        <polygon points="453,136 585,0 680,0 680,136" fill="url(#patternLight)"/>
      </svg>
    </section>

    <section class="billboard billboard--dark">
      <div class="brand-square"></div>
      <div class="brand-name">Velmora</div>
      <div class="web-address">www.velmora.hr</div>
      <svg class="pattern-field" viewBox="0 0 680 136" role="img" aria-label="Orange geometric chevron pattern in the right corner">
        <defs>
          <linearGradient id="patternDark" x1="0" y1="1" x2="1" y2="0">
            <stop offset="0" stop-color="var(--orange-deep)"/>
            <stop offset="1" stop-color="var(--orange-light)"/>
          </linearGradient>
        </defs>
        <polygon points="450,136 582,0 680,0 680,136" fill="url(#patternDark)"/>
      </svg>
    </section>
  </main>
</body>
</html>
```